TARPLOAD business card design

TARPLOAD is a manufacturer of skip bags supplying both the domestic and commercial market. We wish to convey core characteristics of strength, professionalism and reliability to our customers. We are after a business card that uses our company colours of black and yellow as well as incorporating our logo. Our customers are predominantly in the construction or hardware industry. It is important the cards are professional as we are a small company wishing to appear larger than we actually are. more info on the company and product available at www.tarpload-example.com.au

Target Market(s)

hardware buyers, contruction company owners

Industry/Entity Type

Construction

Requirements
Must have
• company colours of black and yellow - No other colours or variation of yellow black. our company logo. card design must convey "tough"
• Card design must be landscape
• Details to be included on the card are:
• Name and Tiltle
• Phone number : 1300 41 62 53
• Mobile: 0452 718 903
• Fax: 03 9617 4852
• email: dale.hendry@tarpload-example.com.au
• address: PO Box 517, Kelvindale, VIC,3294
• Text in white when on a black background
Nice to have
• I like the idea of the back of the card being black with lighter circle area in the middle with black logo in the centre. Similar to the attached "iconic" card

```html
<!DOCTYPE html>
<html lang="en">
<head>
<meta charset="utf-8">
<title>TARPLOAD business card</title>
<link rel="stylesheet" href="https://fonts.googleapis.com/css2?family=Orbitron:wght@500;700;800&display=swap">
<style>
  :root {
    --yellow: #f0c900;
    --black: #141414;
    --ink: #1a1a1a;
    --page: #ffffff;
  }
  * { margin: 0; padding: 0; box-sizing: border-box; }
  html, body {
    width: 1080px; height: 1200px; overflow: hidden;
    background: var(--page);
    font-family: "Orbitron", sans-serif;
  }
  .card {
    position: absolute; left: 49px; width: 979px; height: 541px; overflow: hidden;
  }
  .card--front { top: 42px; background: var(--yellow); }
  .card--back  { top: 612px; background: var(--black); }

  .band { position: absolute; left: 0; width: 100%; background: var(--black); }
  .band--top { top: 0; height: 34px; }
  .band--bottom { bottom: 0; height: 36px; }

  .stripe { position: absolute; inset: 0; }

  .brand {
    position: absolute; display: flex; align-items: center; gap: 12px;
    color: var(--ink); font-weight: 800; letter-spacing: 1px;
  }
  .brand__square { background: var(--ink); flex: none; }
  .card--front .brand { left: 62px; top: 170px; font-size: 34px; }
  .card--front .brand__square { width: 26px; height: 26px; }

  .person { position: absolute; left: 341px; top: 172px; color: var(--ink); }
  .person__name { font-size: 37px; font-weight: 800; letter-spacing: 2px; text-transform: uppercase; }
  .person__title { font-size: 19px; font-weight: 500; letter-spacing: 1.5px; text-transform: uppercase; font-style: italic; margin-top: 6px; }

  .contact { list-style: none; position: absolute; left: 0; top: 0; color: var(--ink); }
  .contact li {
    position: absolute; white-space: nowrap; font-size: 18px; font-weight: 500;
    letter-spacing: 1.5px; text-transform: uppercase; font-style: italic;
  }
  .contact__phone  { left: 341px; top: 278px; }
  .contact__mobile { left: 356px; top: 304px; }
  .contact__fax    { left: 371px; top: 330px; }
  .contact__email  { left: 392px; top: 356px; }
  .contact__post   { left: 407px; top: 382px; }

  .website {
    position: absolute; right: 56px; top: 438px; color: var(--ink);
    font-size: 21px; font-weight: 700; letter-spacing: 1.5px; text-transform: uppercase; font-style: italic;
  }

  .glow {
    position: absolute; left: 264px; top: 30px; width: 480px; height: 480px; border-radius: 50%;
    background: radial-gradient(circle, #f2d35a 0%, #c9ac3a 35%, #6b5d25 60%, rgba(20,20,20,0) 72%);
  }
  .card--back .brand { left: 50%; top: 50%; transform: translate(-50%, -50%); font-size: 52px; }
  .card--back .brand__square { width: 38px; height: 38px; }
</style>
</head>
<body>
  <section class="card card--front">
    <div class="band band--top"></div>
    <svg class="stripe" viewBox="0 0 979 541" aria-hidden="true">
      <polygon points="70,286 262,286 330,418 312,418 252,298 70,298" fill="#141414"/>
      <polygon points="338,434 360,434 368,450 346,450" fill="#141414"/>
      <polygon points="352,464 378,464 386,480 360,480" fill="#141414"/>
      <polygon points="366,494 398,494 424,541 388,541" fill="#141414"/>
    </svg>
    <div class="brand"><span class="brand__square"></span>TARPLOAD</div>
    <div class="person">
      <div class="person__name">Dale Hendry</div>
      <div class="person__title">Managing Director</div>
    </div>
    <ul class="contact">
      <li class="contact__phone">Phone: 1300 41 62 53</li>
      <li class="contact__mobile">Mobile: 0452 718 903</li>
      <li class="contact__fax">Fax: 03 9617 4852</li>
      <li class="contact__email">dale.hendry@tarpload-example.com.au</li>
      <li class="contact__post">PO Box 517, Kelvindale, VIC,3294</li>
    </ul>
    <div class="website">www.tarpload-example.com.au</div>
    <div class="band band--bottom"></div>
  </section>

  <section class="card card--back">
    <div class="glow"></div>
    <div class="brand"><span class="brand__square"></span>TARPLOAD</div>
  </section>
</body>
</html>
```